Commercial Landscaping Flyer Needed

Looking for a flyer design to showcase what we offer for commercial landscape Installations. We want this to illustrate what sets us apart from our competitors. Include our EMR Safety rating of .72, that our average commercial landscape installation size is $215,000 with our largest completed in 2020 being $1,375,590. We have backgrounds in commercial design and installation and help our customers with Value Engineering Strategies. Since incorporating in 2005, we have an average employment retention length of 8 years. We want this flyer to show our commercial clients that we mean business and are dedicated to making their project happen on time, run efficiently, and we do excellent work.

Need extra days to review

```html
<!DOCTYPE html>
<html lang="en">
<head>
<meta charset="utf-8">
<title>Verdant Ridge Inc. – Commercial Landscape Installations</title>
<link rel="stylesheet" href="https://fonts.googleapis.com/css2?family=Open+Sans:wght@400;600;700;800&family=Oswald:wght@600;700&display=swap">
<style>
  :root {
    --lime: #c2d92f;
    --lime-text: #b5d12a;
    --ink: #0b0b0b;
    --white: #ffffff;
    --paper: #f7f7f7;
    --grey: #e6e6e6;
    --shield-a: #1a8fe0;
    --shield-b: #39c7f5;
  }
  * { box-sizing: border-box; margin: 0; padding: 0; }
  html, body { width: 990px; height: 1200px; overflow: hidden; background: var(--white); }
  body { font-family: "Open Sans", Arial, sans-serif; color: var(--ink); }

  .flyer {
    position: relative;
    width: 990px;
    height: 1200px;
    overflow: hidden;
    background: linear-gradient(135deg, var(--white) 0%, var(--paper) 45%, var(--grey) 100%);
  }

  /* Header */
  .brand {
    position: absolute; left: 72px; top: 118px;
    display: flex; align-items: center; gap: 14px;
  }
  .brand-dot { width: 34px; height: 34px; border-radius: 50%; background: var(--lime); }
  .brand-name { font-size: 34px; font-weight: 800; color: var(--ink); letter-spacing: -0.5px; }

  .website {
    position: absolute; left: 545px; top: 84px;
    display: flex; align-items: center; gap: 10px;
    font-size: 18px; letter-spacing: 2.6px; color: var(--ink);
  }
  .website b { font-weight: 800; }

  /* Photo circle */
  .hero-photo {
    position: absolute; left: 382px; top: 150px;
    width: 556px; height: 556px; border-radius: 50%;
    border: 13px solid var(--lime);
    background: radial-gradient(circle at 40% 60%, #5f9a3c 0%, #8a9a7a 40%, #b5a79a 60%, #6b6f72 100%);
  }

  /* Headline circle */
  .headline {
    position: absolute; left: 53px; top: 255px;
    width: 464px; height: 464px; border-radius: 50%;
    border: 14px solid var(--ink);
    background: var(--lime);
    overflow: hidden;
    text-align: center;
  }
  .headline-intro { position: absolute; left: 0; right: 0; top: 62px; font-size: 40px; font-weight: 800; line-height: 1.13; }
  .headline-rule { position: absolute; left: 55px; right: 55px; top: 170px; height: 3px; background: var(--ink); }
  .headline-band { position: absolute; left: 0; right: 0; top: 235px; height: 66px; background: var(--ink); }
  .headline-word {
    position: absolute; left: 0; right: 0;
    font-family: "Oswald", "Arial Narrow", sans-serif; font-weight: 700;
    font-size: 52px; line-height: 1; letter-spacing: 1px;
  }
  .headline-word.commercial { top: 180px; }
  .headline-word.landscape { top: 241px; color: var(--white); }
  .headline-word.installations { top: 302px; }

  /* Stats */
  .stat-block {
    position: absolute; left: 74px; top: 735px; width: 450px;
    border-left: 3px solid var(--lime);
    padding-left: 18px;
    font-size: 20px; font-weight: 700; line-height: 28px;
  }
  .highlight { color: var(--lime-text); }

  /* Safety rating */
  .safety { position: absolute; left: 580px; top: 726px; width: 340px; height: 130px; }
  .safety-shield { position: absolute; left: 0; top: 0; }
  .emr-label {
    position: absolute; left: 121px; top: 24px; width: 147px; height: 46px;
    background: var(--lime);
    font-size: 44px; font-weight: 800; line-height: 46px; padding-left: 16px;
  }
  .safety-label {
    position: absolute; left: 121px; top: 71px; width: 219px; height: 38px;
    background: var(--ink); color: var(--lime);
    font-size: 24px; font-weight: 700; line-height: 38px; padding-left: 22px;
  }

  .about {
    position: absolute; left: 582px; width: 345px;
    border-left: 3px solid var(--lime); padding-left: 19px;
    font-size: 18px; font-weight: 600; line-height: 26px;
  }
  .about.backgrounds { top: 860px; }
  .about.retention { top: 972px; }

  /* Services */
  .services {
    position: absolute; left: 59px; top: 893px; width: 451px; height: 150px;
    background: var(--lime);
    border: 2px solid #d5d5d5;
    border-radius: 0 8px 0 8px;
  }
  .services-title {
    position: absolute; left: 90px; top: 872px; height: 42px; width: 290px;
    background: var(--ink); color: var(--lime);
    font-size: 29px; font-weight: 700; line-height: 42px; padding-left: 20px;
    clip-path: polygon(0 0, 90% 0, 100% 100%, 0 100%);
  }
  .service-list { position: absolute; list-style: none; font-size: 18px; font-weight: 600; }
  .service-list li { display: flex; align-items: center; gap: 7px; height: 27px; }
  .service-list.left { left: 80px; top: 925px; }
  .service-list.right { left: 302px; top: 979px; }
  .service-list.left li.wide { margin-bottom: 0; }

  /* Call to action */
  .cta-band { position: absolute; left: 0; right: 0; top: 1098px; bottom: 0; background: var(--lime); }
  .cta-bar {
    position: absolute; left: 59px; top: 1060px; width: 871px; height: 67px;
    background: var(--ink); border-radius: 0 8px 8px 0;
    color: var(--white); text-align: center;
    font-size: 47px; font-weight: 800; line-height: 67px; letter-spacing: 0.5px;
  }
  .cta-bar span { color: var(--lime); }
  .phones {
    position: absolute; left: 0; right: 0; top: 1128px;
    display: flex; justify-content: center; align-items: center; gap: 18px;
    font-size: 43px; font-weight: 800; line-height: 56px;
  }
  .phone { display: flex; align-items: center; gap: 10px; }
  .divider { width: 3px; height: 40px; background: var(--ink); }
</style>
</head>
<body>
<main class="flyer">

  <div class="brand">
    <span class="brand-dot"></span>
    <span class="brand-name">Verdant Ridge Inc.</span>
  </div>

  <div class="website">
    <svg width="20" height="20" viewBox="0 0 20 20" fill="none" stroke="#b5d12a" stroke-width="1.8">
      <circle cx="10" cy="10" r="8.5"/><ellipse cx="10" cy="10" rx="3.8" ry="8.5"/><line x1="1.5" y1="10" x2="18.5" y2="10"/>
    </svg>
    <span>www.<b>VerdantRidgeInc</b>.com</span>
  </div>

  <div class="hero-photo" role="img" aria-label="Aerial photo of a finished rooftop courtyard with artificial turf, paved patio, seating and planters between apartment buildings"></div>

  <section class="headline">
    <p class="headline-intro">we are<br>specialised in</p>
    <div class="headline-rule"></div>
    <div class="headline-band"></div>
    <h1>
      <span class="headline-word commercial">COMMERCIAL</span>
      <span class="headline-word landscape">LANDSCAPE</span>
      <span class="headline-word installations">INSTALLATIONS</span>
    </h1>
  </section>

  <p class="stat-block">Our average commercial landscape installation size is <span class="highlight">$215,000</span> with our largest completed in 2020 being <span class="highlight">$1,375,590.</span></p>

  <div class="safety">
    <svg class="safety-shield" width="124" height="130" viewBox="0 0 124 130">
      <defs>
        <linearGradient id="shieldFill" x1="0" y1="0" x2="1" y2="1">
          <stop offset="0" stop-color="var(--shield-b)"/><stop offset="1" stop-color="var(--shield-a)"/>
        </linearGradient>
      </defs>
      <path d="M62 2 L120 16 L116 70 Q108 108 62 128 Q16 108 8 70 L4 16 Z" fill="#c9ced3" stroke="#9aa3ab" stroke-width="2"/>
      <path d="M62 10 L112 22 L108 70 Q100 102 62 120 Q24 102 16 70 L12 22 Z" fill="url(#shieldFill)"/>
      <text x="62" y="82" text-anchor="middle" font-family="Oswald, sans-serif" font-weight="700" font-size="56" fill="#ffffff">.72</text>
    </svg>
    <div class="emr-label">EMR</div>
    <div class="safety-label">Safety Rating</div>
  </div>

  <p class="about backgrounds">We have backgrounds in commercial design and installation and help our customers with Value Engineering Strategies.</p>
  <p class="about retention">Since incorporating in 2005, we have an average employment retention length of 8 years.</p>

  <div class="services"></div>
  <h2 class="services-title">OUR SERVICES</h2>
  <ul class="service-list left">
    <li><svg width="16" height="16" viewBox="0 0 16 16" fill="none" stroke="#0b0b0b" stroke-width="1.4"><circle cx="8" cy="8" r="7"/><path d="M4.5 8.2 L7 10.5 L11.5 5.5"/></svg>Maintenance</li>
    <li><svg width="16" height="16" viewBox="0 0 16 16" fill="none" stroke="#0b0b0b" stroke-width="1.4"><circle cx="8" cy="8" r="7"/><path d="M4.5 8.2 L7 10.5 L11.5 5.5"/></svg>Chemical Applications &amp; Fertilization</li>
    <li><svg width="16" height="16" viewBox="0 0 16 16" fill="none" stroke="#0b0b0b" stroke-width="1.4"><circle cx="8" cy="8" r="7"/><path d="M4.5 8.2 L7 10.5 L11.5 5.5"/></svg>Turf Management</li>
    <li><svg width="16" height="16" viewBox="0 0 16 16" fill="none" stroke="#0b0b0b" stroke-width="1.4"><circle cx="8" cy="8" r="7"/><path d="M4.5 8.2 L7 10.5 L11.5 5.5"/></svg>Irrigation</li>
  </ul>
  <ul class="service-list right">
    <li><svg width="16" height="16" viewBox="0 0 16 16" fill="none" stroke="#0b0b0b" stroke-width="1.4"><circle cx="8" cy="8" r="7"/><path d="M4.5 8.2 L7 10.5 L11.5 5.5"/></svg>Hardscaping</li>
    <li><svg width="16" height="16" viewBox="0 0 16 16" fill="none" stroke="#0b0b0b" stroke-width="1.4"><circle cx="8" cy="8" r="7"/><path d="M4.5 8.2 L7 10.5 L11.5 5.5"/></svg>Landscaping</li>
  </ul>

  <div class="cta-band"></div>
  <div class="cta-bar">CALL NOW FOR A <span>FREE QUOTE</span></div>
  <div class="phones">
    <span class="phone">
      <svg width="40" height="40" viewBox="0 0 40 40" fill="none" stroke="#0b0b0b" stroke-width="3"><circle cx="20" cy="20" r="17.5"/><path d="M14 11 L17 11 L18.5 16 L16.5 17.5 Q18 22.5 22.5 24 L24 22 L29 23.5 L29 26.5 Q27 29.5 23 28.5 Q13 25 11.5 15 Q11.5 12 14 11 Z" fill="#0b0b0b" stroke-width="1"/></svg>
      (555) 201-4478
    </span>
    <span class="divider"></span>
    <span class="phone">
      <svg width="40" height="40" viewBox="0 0 40 40" fill="none" stroke="#0b0b0b" stroke-width="3"><circle cx="20" cy="20" r="17.5"/><path d="M14 11 L17 11 L18.5 16 L16.5 17.5 Q18 22.5 22.5 24 L24 22 L29 23.5 L29 26.5 Q27 29.5 23 28.5 Q13 25 11.5 15 Q11.5 12 14 11 Z" fill="#0b0b0b" stroke-width="1"/></svg>
      (555) 318-6023
    </span>
  </div>

</main>
</body>
</html>
```